Offshore Energy Projects Management Consultancy needs a business card design

Logo available. We provide teams to deliver engineering consultancy, project management and delivery teams mainly in the offshore renewables sector. The company is all about bringing the right people to a project to deliver the scope.

The business card will be used for all staff.

The business card should be quite simple, vibrant and uncluttered but convey experience, enthusiasm and integration.

Target Market(s)

Energy Project Developers and Tier 1 construction companies

Contact Information for Business Card

Logo should be on the back of the card. I'm happy for the designer to play with the colour of the logo and background colour.

Front of the card should convey all the must have information in a clear and professional manner but without being overly traditional.

Colors

Designer to choose colors to be used in the design.

Requirements
Must have
• Land Line Tel Number, Mobile Tel Number, Email, business address, web address.

```html
<!DOCTYPE html>
<html lang="en">
<head>
<meta charset="utf-8">
<title>Tideline Projects Alliance – Business Card</title>
<link rel="stylesheet" href="https://fonts.googleapis.com/css2?family=Lato:wght@400;700&family=Poppins:wght@500;600&display=swap">
<style>
  :root {
    --page-bg: #ececec;
    --card-dark: #2a2a2a;
    --card-light: #ffffff;
    --brand-blue: #29a8df;
    --brand-deep: #1a6fc0;
    --ink: #1e1e1e;
    --ink-soft: #444444;
    --band-grey: #6e6e6e;
  }
  * { margin: 0; padding: 0; box-sizing: border-box; }
  html, body { width: 1200px; height: 757px; overflow: hidden; }
  body {
    background: var(--page-bg);
    position: relative;
    font-family: "Lato", Arial, sans-serif;
  }
  .card {
    position: absolute;
    top: 195px;
    width: 499px;
    height: 299px;
    overflow: hidden;
  }
  .card--back { left: 90px; background: var(--card-dark); }
  .card--front { left: 650px; background: var(--card-light); }

  /* Back */
  .back-brand {
    position: absolute;
    top: 105px;
    left: 0;
    right: 0;
    display: flex;
    align-items: center;
    justify-content: center;
    gap: 14px;
  }
  .brand-dot {
    width: 34px;
    height: 34px;
    border-radius: 50%;
    background: var(--brand-blue);
  }
  .back-brand .brand-name {
    font-family: "Poppins", Arial, sans-serif;
    font-weight: 600;
    font-size: 27px;
    line-height: 1.15;
    color: var(--brand-blue);
    letter-spacing: 0.5px;
  }
  .back-web {
    position: absolute;
    bottom: 29px;
    left: 0;
    right: 0;
    text-align: center;
    font-family: "Poppins", Arial, sans-serif;
    font-weight: 500;
    font-size: 11px;
    letter-spacing: 3px;
    color: var(--brand-blue);
  }

  /* Front */
  .front-brand {
    position: absolute;
    top: 46px;
    left: 0;
    right: 0;
    display: flex;
    align-items: center;
    justify-content: center;
    gap: 9px;
  }
  .front-brand .brand-dot { width: 22px; height: 22px; }
  .front-brand .brand-name {
    font-family: "Poppins", Arial, sans-serif;
    font-weight: 600;
    font-size: 17px;
    color: var(--brand-blue);
    letter-spacing: 0.3px;
  }
  .contact-tab {
    position: absolute;
    left: 0;
    top: 175px;
    width: 40px;
    height: 89px;
    background: var(--brand-blue);
    border-radius: 0 8px 8px 0;
  }
  .contact-tab svg { position: absolute; left: 11px; width: 18px; height: 18px; }
  .contact-list {
    position: absolute;
    left: 45px;
    top: 177px;
    list-style: none;
    font-size: 11.5px;
    color: var(--ink);
    line-height: 1.3;
  }
  .contact-list li { margin-bottom: 9px; }
  .contact-list li.address { margin-top: -1px; }
  .person {
    position: absolute;
    right: 31px;
    top: 199px;
    text-align: right;
  }
  .person-name {
    font-weight: 700;
    font-size: 16px;
    color: var(--brand-deep);
  }
  .person-role {
    font-size: 8px;
    color: var(--ink-soft);
    letter-spacing: 0.2px;
    margin-top: 1px;
  }
  .front-bands { position: absolute; left: 0; bottom: 0; width: 499px; height: 16px; }
</style>
</head>
<body>
  <section class="card card--back" aria-label="Card back">
    <div class="back-brand">
      <span class="brand-dot"></span>
      <span class="brand-name">Tideline Projects Alliance</span>
    </div>
    <p class="back-web">www.tidelineprojects.com</p>
  </section>

  <section class="card card--front" aria-label="Card front">
    <div class="front-brand">
      <span class="brand-dot"></span>
      <span class="brand-name">Tideline Projects Alliance</span>
    </div>

    <div class="contact-tab" aria-hidden="true">
      <svg style="top:8px" viewBox="0 0 24 24"><path fill="#fff" d="M6.6 10.8c1.4 2.8 3.8 5.1 6.6 6.6l2.2-2.2c.3-.3.7-.4 1-.2 1.1.4 2.3.6 3.6.6.6 0 1 .4 1 1V20c0 .6-.4 1-1 1C10.6 21 3 13.4 3 4c0-.6.4-1 1-1h3.5c.6 0 1 .4 1 1 0 1.3.2 2.5.6 3.6.1.3 0 .7-.2 1l-2.3 2.2z"/></svg>
      <svg style="top:35px" viewBox="0 0 24 24"><rect x="3" y="5" width="18" height="14" rx="1" fill="none" stroke="#fff" stroke-width="2"/><path d="M3 6l9 7 9-7" fill="none" stroke="#fff" stroke-width="2"/></svg>
      <svg style="top:62px" viewBox="0 0 24 24"><circle cx="12" cy="12" r="9" fill="none" stroke="#fff" stroke-width="2"/><path d="M3 12h18M12 3c3 3 3 15 0 18M12 3c-3 3-3 15 0 18" fill="none" stroke="#fff" stroke-width="1.6"/></svg>
    </div>

    <ul class="contact-list">
      <li>555-014-2290, ext 1172</li>
      <li>mholt@tidelinegroup.org</li>
      <li class="address">2750 Harbor Crest, Suite 310<br>Fairview, Kansas 66000</li>
    </ul>

    <div class="person">
      <p class="person-name">Maren Holt</p>
      <p class="person-role">PROGRAM COORDINATOR</p>
    </div>

    <svg class="front-bands" viewBox="0 0 499 16" aria-hidden="true">
      <rect x="0" y="4" width="310" height="12" fill="var(--band-grey)"/>
      <path d="M300 16 C306 4 312 2 330 2 L499 2 L499 16 Z" fill="#fff"/>
      <path d="M306 16 C312 6 318 4 334 4 L499 4 L499 16 Z" fill="var(--brand-blue)"/>
    </svg>
  </section>
</body>
</html>
```